Flyer/Poster design required for volunteer activities

We need a STRIKING A4 Poster/Flyer advertising our conservation volunteer program activities which are currently happening in the area. This poster is to advertise the program once people have arrived on the island or to locals. The program covers 5 months, May-September 2019 and is focused on conservation. I have attached the following:
- a flyer which was previously created (QMR Habitat Helpers 2019 sm)to advertise the program - would prefer it has a similar striking resemblance, but not essential
- A mock up document 'HHQMR On Island Poster_2019_v2' with text -Logos-Images

Target Market(s)

Everyone interested in Environmental Adventure/Hiking/Citizen Science

Industry/Entity Type

Tourism

Font styles to use
Sans Serif

Requirements
Must have
• -A travel conservation focus
• -Must use 'QMR-Background Image' as the background to the design
• -The info of where to get more information and the social media details must be prominent

```html
<!DOCTYPE html>
<html lang="en">
<head>
<meta charset="utf-8">
<title>QMR Habitat Helpers 2019</title>
<link href="https://fonts.googleapis.com/css2?family=Open+Sans:wght@600;700;800&family=PT+Sans+Narrow:wght@400;700&display=swap" rel="stylesheet">
<style>
  :root {
    --sky-pale: #e3eef7;
    --sky-mid: #c5dbec;
    --navy: #1d4e86;
    --navy-deep: #1a2f5c;
    --orange: #f0a22e;
    --gold: #f4b23c;
    --panel: rgba(222, 236, 248, 0.72);
  }
  * { box-sizing: border-box; margin: 0; padding: 0; }
  html, body { width: 1200px; height: 851px; overflow: hidden; background: #ffffff; }
  .poster { position: relative; width: 1200px; height: 851px; display: flex; }

  /* Left cover side */
  .cover {
    position: relative; width: 600px; height: 851px;
    background: linear-gradient(180deg, var(--sky-pale) 0%, var(--sky-mid) 100%);
  }
  .cover__hexes { position: absolute; left: 0; top: 0; width: 600px; height: 851px; }
  .brand {
    position: absolute; left: 92px; top: 118px; width: 200px;
    display: flex; align-items: center; justify-content: center; gap: 10px;
    font-family: "PT Sans Narrow", sans-serif; font-weight: 700;
    font-size: 28px; line-height: 1.05; color: var(--navy);
  }
  .brand__dot { width: 28px; height: 28px; border-radius: 50%; background: var(--navy); flex: none; }

  .cover__titles { position: absolute; left: 40px; top: 614px; font-family: "PT Sans Narrow", sans-serif; }
  .cover__place { font-size: 39px; font-weight: 700; color: var(--navy); line-height: 1; letter-spacing: 0.2px; }
  .cover__program { font-size: 32px; font-weight: 700; color: var(--navy); line-height: 1.15; margin-top: 6px; }
  .cover__dates { font-size: 22px; font-weight: 700; color: var(--orange); line-height: 1; }
  .cover__tagline { margin-top: 18px; font-family: "Open Sans", sans-serif; font-weight: 700; font-size: 20px; color: var(--navy); line-height: 1.25; }
  .cover__join { font-family: "Open Sans", sans-serif; font-weight: 700; font-size: 17px; color: var(--navy); line-height: 1.4; }

  .cover__info {
    position: absolute; left: 0; width: 600px; top: 812px; text-align: center;
    font-family: "Open Sans", sans-serif; font-weight: 700; font-style: italic;
    font-size: 6.5px; color: var(--navy-deep); line-height: 1.35;
  }

  /* Right schedule side */
  .schedule {
    position: relative; width: 600px; height: 851px; overflow: hidden;
    background:
      radial-gradient(ellipse 180px 320px at 540px 330px, #4f6f58 0%, rgba(79,111,88,0) 100%),
      radial-gradient(ellipse 260px 200px at 160px 560px, #6b8a6a 0%, rgba(107,138,106,0) 100%),
      radial-gradient(ellipse 200px 160px at 500px 760px, #556f5c 0%, rgba(85,111,92,0) 100%),
      linear-gradient(180deg, #c9d7e3 0%, #a8c3d8 12%, #4f8fb4 30%, #3d86ab 55%, #5f9488 75%, #4b6f5e 100%);
  }
  .schedule__photo { position: absolute; inset: 0; }
  .schedule__panel {
    position: absolute; left: 106px; top: 60px; width: 386px; height: 708px;
    background: var(--panel); padding: 8px 12px 0 14px;
    font-family: "Open Sans", sans-serif; color: var(--navy-deep);
  }
  .month { text-align: center; font-weight: 800; color: var(--gold); font-size: 17px; line-height: 1.1; }
  .feature { text-align: center; font-weight: 700; color: var(--orange); font-size: 12px; line-height: 1.3; margin-bottom: 26px; }
  .topic { font-weight: 800; font-size: 9px; line-height: 1.35; }
  .activities { list-style: none; font-weight: 700; font-size: 8.8px; line-height: 1.4; margin-bottom: 20px; }
  .activities li::before { content: "-"; }
</style>
</head>
<body>
<div class="poster">

  <section class="cover">
    <svg class="cover__hexes" viewBox="0 0 500 709">
      <defs>
        <linearGradient id="mountainTone" x1="0" y1="0" x2="0" y2="1">
          <stop offset="0" stop-color="#b9d3ea"/><stop offset="0.55" stop-color="#6f9fc2"/><stop offset="1" stop-color="#56704c"/>
        </linearGradient>
        <linearGradient id="forestTone" x1="0" y1="0" x2="1" y2="1">
          <stop offset="0" stop-color="#8aa463"/><stop offset="0.6" stop-color="#5f6e3c"/><stop offset="1" stop-color="#7e6a4a"/>
        </linearGradient>
        <linearGradient id="reefTone" x1="0" y1="0" x2="0" y2="1">
          <stop offset="0" stop-color="#5db3d6"/><stop offset="0.6" stop-color="#2f7fb1"/><stop offset="1" stop-color="#1d5f8f"/>
        </linearGradient>
      </defs>
      <polygon points="160,18 262,77 262,195 160,254 58,195 58,77" fill="none" stroke="#ffffff" stroke-opacity="0.75" stroke-width="6"/>
      <polygon points="345,82 452,144 452,268 345,330 238,268 238,144" fill="#eef5fb" fill-opacity="0.6"/>
      <polygon role="img" aria-label="Photo of a hiker with backpack standing on a summit overlooking the lagoon and sea" points="345,95 441,150 441,262 345,317 249,262 249,150" fill="url(#mountainTone)"/>
      <polygon points="158,218 262,278 262,398 158,458 54,398 54,278" fill="#eef5fb" fill-opacity="0.6"/>
      <polygon role="img" aria-label="Photo of a hiker walking through dense palm forest" points="158,231 251,285 251,391 158,445 65,391 65,285" fill="url(#forestTone)"/>
      <polygon points="345,283 456,347 456,475 345,539 234,475 234,347" fill="#eef5fb" fill-opacity="0.6"/>
      <polygon role="img" aria-label="Photo of a snorkeller recording data on a slate underwater above coral" points="345,297 444,354 444,468 345,525 246,468 246,354" fill="url(#reefTone)"/>
    </svg>

    <div class="brand"><span class="brand__dot"></span><span>QMR Habitat<br>Helpers</span></div>

    <div class="cover__titles">
      <div class="cover__place">QUEEN MARA ISLAND</div>
      <div class="cover__program">HABITAT HELPERS</div>
      <div class="cover__dates">May – September 2019</div>
      <div class="cover__tagline">BE INVOLVED IN PROTECTING PARADISE</div>
      <div class="cover__join">JOIN THE QMR HABITAT HELPERS PROGRAM 2019</div>
    </div>

    <div class="cover__info">
      See the QMR visitor centre for more information about the QMR Habitat Helpers program for 2019<br>
      FOLLOW US! &nbsp; www.friendloop.net/hhqmr &nbsp;&nbsp; snapgrid@hhqmr
    </div>
  </section>

  <section class="schedule">
    <div class="schedule__photo" role="img" aria-label="Aerial photo of the island with lagoon, beaches and mountains under a pale sky"></div>
    <div class="schedule__panel">
      <div class="month">MAY 2019</div>
      <div class="feature">Feature Week: 19th – 26th May</div>
      <div class="topic">BIRDS OF QUEEN MARA ISLAND</div>
      <ul class="activities">
        <li>Ocean bird watching boat trips</li>
        <li>Guided tours of Woodhen and Currawong quarters</li>
        <li>Weekly lectures at the Queen Mara Island Museum</li>
        <li>Weekly screenings of documentaries on Bird and Island Conservation projects</li>
        <li>Self guided land bird survey tours</li>
      </ul>

      <div class="month">JUNE 2019</div>
      <div class="feature">Feature Week: 3rd – 9th June</div>
      <div class="topic">QUEEN MARA ISLAND MARINE PARK</div>
      <ul class="activities">
        <li>Marine pest monitoring with marine park staff</li>
        <li>Marine plastic &amp; debris clean up activities</li>
        <li>Screenings of marine conservation documentaries at the museum</li>
        <li>Weekly lectures on Marine Life at the Queen Mara Island Museum</li>
        <li>Marine Activities with local operators</li>
      </ul>

      <div class="month">JULY 2019</div>
      <div class="feature">Feature Week: 21st – 28th July</div>
      <div class="topic">INVASIVE SPECIES</div>
      <ul class="activities">
        <li>Guided walks to learn about the weed eradication program</li>
        <li>Weekly lectures on plants of Queen Mara Island</li>
        <li>Weekly screenings of documentaries on plant and island conservation projects</li>
        <li>Guided walks to Mount Ardell</li>
        <li>Local tour guides include commentaries on island plants</li>
      </ul>

      <div class="month">AUGUST 2019</div>
      <div class="feature">Feature Week: 11th – 18th August</div>
      <div class="topic">AMAZING INVERTEBRATES</div>
      <ul class="activities">
        <li>Guided night walks to learn about the island's invertebrates</li>
        <li>Weekly viewing and presentation of the Queen Mara Island Phasmid</li>
        <li>Weekly lectures on invertebrates of Queen Mara Island at the museum</li>
        <li>Weekly screenings of documentaries on island conservation projects</li>
      </ul>

      <div class="month">SEPTEMBER 2019</div>
      <div class="feature">Feature Week: 1st – 8th September</div>
      <div class="topic">PROTECTING PARADISE</div>
      <ul class="activities">
        <li>Observational snorkel surveys with Marine Ecologists, to assess populations of Marlow's Anemonefish and other unique fish species</li>
        <li>Guided snorkel and glass bottom boat tour to assess coral health within the Queen Mara Island Marine Park</li>
        <li>Guided walks to learn about the island's conservation history</li>
      </ul>
    </div>
  </section>

</div>
</body>
</html>
```